2 x storefront vinyl request

We are transitioning to a storefront office and need two vinyls for the windows.

First vinyl: Use the Dalton Rivers logo, website (www.daltonriversholdings.example) and leasing office number ((555) 318-4472)

Second vinyl: Maintenance Division & phone number (555) 318-4472

```html
<!DOCTYPE html>
<html lang="en">
<head>
<meta charset="utf-8">
<title>Dalton Rivers Properties – Storefront Vinyls</title>
<link rel="stylesheet" href="https://fonts.googleapis.com/css2?family=Barlow+Condensed:wght@600;700&display=swap">
<style>
  :root {
    --bg: #e3e7e9;
    --card: #ffffff;
    --ink: #2f2f31;
    --text: #3b3b3d;
    --band-light: #e6e7e8;
    --band-mid: #c9cacc;
    --band-dark: #a6a6a8;
    --sheen: #f1f1f2;
  }
  * { margin: 0; padding: 0; box-sizing: border-box; }
  html, body { width: 1200px; height: 965px; overflow: hidden; background: var(--bg); }
  body { position: relative; font-family: "Barlow Condensed", "Arial Narrow", sans-serif; color: var(--text); }

  .vinyl {
    position: absolute; top: 104px; width: 428px; height: 754px;
    background: var(--card); overflow: hidden;
  }
  .vinyl--leasing { left: 132px; }
  .vinyl--maintenance { left: 640px; }

  .vinyl__backdrop { position: absolute; inset: 0; width: 100%; height: 100%; }

  .header-band {
    position: absolute; left: 0; top: 38px; width: 100%; height: 116px;
    background: var(--band-light);
    text-align: center;
  }
  .header-band__label { font-weight: 600; font-size: 23px; letter-spacing: 0.3px; margin-top: 16px; line-height: 1; }
  .header-band__phone { font-weight: 700; font-size: 54px; line-height: 1; margin-top: 6px; }

  .division-title {
    position: absolute; left: 0; top: 38px; width: 100%;
    text-align: center; font-weight: 700; font-size: 60px; line-height: 1; letter-spacing: 0.5px;
  }

  .wordmark {
    position: absolute; left: 0; top: 300px; width: 100%; height: 200px;
    display: flex; align-items: center; justify-content: center; gap: 22px;
  }
  .wordmark__square { flex: none; width: 96px; height: 96px; background: var(--ink); }
  .wordmark__name {
    font-weight: 700; font-size: 44px; line-height: 0.98;
    color: var(--ink); text-transform: uppercase;
  }

  .footer-band {
    position: absolute; left: 0; top: 640px; width: 100%; height: 80px;
    background: var(--band-light);
    display: flex; align-items: center; justify-content: center;
  }
  .footer-band__web { font-weight: 700; font-size: 28px; }
  .footer-band__phone { font-weight: 700; font-size: 54px; line-height: 1; }
  .footer-strip { position: absolute; left: 0; top: 720px; width: 100%; height: 34px; background: var(--band-dark); }
</style>
</head>
<body>

  <section class="vinyl vinyl--leasing">
    <svg class="vinyl__backdrop" viewBox="0 0 428 754" aria-hidden="true">
      <polygon points="0,480 0,754 300,754" fill="var(--band-dark)"/>
      <polygon points="60,390 260,200 300,200 100,390 100,560 60,520" fill="var(--sheen)"/>
      <polygon points="20,520 230,230 280,230 70,520 280,754 220,754" fill="var(--band-light)" opacity="0.7"/>
      <polygon points="0,600 120,470 160,470 40,600 180,754 130,754" fill="var(--band-mid)" opacity="0.5"/>
    </svg>
    <div class="header-band">
      <p class="header-band__label">LEASING OFFICE NUMBER</p>
      <p class="header-band__phone">(555) 318-4472</p>
    </div>
    <div class="wordmark">
      <span class="wordmark__square"></span>
      <span class="wordmark__name">Dalton<br>Rivers<br>Properties</span>
    </div>
    <div class="footer-band"><p class="footer-band__web">daltonriversholdings.example</p></div>
    <div class="footer-strip"></div>
  </section>

  <section class="vinyl vinyl--maintenance">
    <svg class="vinyl__backdrop" viewBox="0 0 428 754" aria-hidden="true">
      <polygon points="0,480 0,754 300,754" fill="var(--band-dark)"/>
      <polygon points="60,390 260,200 300,200 100,390 100,560 60,520" fill="var(--sheen)"/>
      <polygon points="20,520 230,230 280,230 70,520 280,754 220,754" fill="var(--band-light)" opacity="0.7"/>
      <polygon points="0,600 120,470 160,470 40,600 180,754 130,754" fill="var(--band-mid)" opacity="0.5"/>
    </svg>
    <h1 class="division-title">MAINTENANCE<br>DIVISION</h1>
    <div class="wordmark">
      <span class="wordmark__square"></span>
      <span class="wordmark__name">Dalton<br>Rivers<br>Properties</span>
    </div>
    <div class="footer-band"><p class="footer-band__phone">(555) 318-4472</p></div>
    <div class="footer-strip"></div>
  </section>

</body>
</html>
```